New banner graphics for Kelbro.com website

I've developed a software tool that helps businesses ensure they are working on their most valuable and important work.

I would like a banner graphic for my home page (www.kelbro.com) that can somehow capture the value of focus and intentional outcomes.

I had an initial thought of a starry sky that shifts focus to a few bright stars, but while that might sound ok, I think my idea is lame hence I'm coming to you guys.

My sites two primary colors are a soft purple and gray.
#919EC1(purple)
#9E9E9E (gray)

Target Market(s)

B2B for enterprises. Typical customers are CFOs, CIOs/Heads of IT

Industry/Entity Type

Business Software

Number of Pages Required

1 page

Font styles to use
Sans Serif

Colors
b8a6cd
cedeed

Requirements
Must have
• I use Divi as my Wordpress theme and the current main landing page can be seen at www.kelbro.com.
• My logo colors are:
• #919EC1(purple)
• #9E9E9E (gray)
Should not have
• Lots of distraction or visual "noise". I want to re-enforce the message that my software is focused on their business and not my products or website.

```html
<!DOCTYPE html>
<html lang="en">
<head>
<meta charset="utf-8">
<title>Kelbro – Waypoint</title>
<link href="https://fonts.googleapis.com/css2?family=Montserrat:wght@400;500;600;700&family=Libre+Baskerville:ital@1&display=swap" rel="stylesheet">
<style>
:root{
  --brand-purple:#919EC1;
  --brand-gray:#9E9E9E;
  --lilac:#b8a6cd;
  --sky:#cedeed;
  --hero:#444444;
  --footer:#1b1b1b;
  --navy:#1a1446;
  --accent-red:#c8102e;
  --link-red:#b0152a;
  --login-green:#4d8a1f;
  --ink:#111111;
  --white:#ffffff;
}
*{margin:0;padding:0;box-sizing:border-box}
html,body{width:720px;height:1200px;overflow:hidden;background:var(--white)}
body{position:relative;font-family:'Montserrat',sans-serif;color:var(--ink)}
.abs{position:absolute}

/* header */
.site-header{left:0;top:0;width:720px;height:70px;background:var(--white)}
.brand{left:72px;top:20px;font-size:27px;font-weight:400;color:var(--brand-gray);letter-spacing:.5px}
.search{left:250px;top:26px;width:245px;height:17px;background:#e3dcea;border:1px solid #b9b0c8;font-size:7.5px;color:#9a94a8;padding:3px 0 0 36px}
.search-btn{left:463px;top:26px;width:32px;height:17px;background:#d3dff0;border:1px solid #b9b0c8}
.social-top{left:500px;top:23px;display:flex;gap:5px}
.social-top span{width:18px;height:18px;border-radius:50%;background:#222}
.login{left:598px;top:22px;font-size:8.5px;color:var(--login-green);line-height:11px}
.login-icon{left:593px;top:24px}
.email{left:301px;top:50px;font-size:10px;font-weight:600;display:flex;align-items:center;gap:5px}
.header-links{left:510px;top:53px;font-size:9.5px;color:var(--link-red);display:flex;gap:13px}

/* hero */
.hero{left:0;top:70px;width:720px;height:240px;background:var(--hero)}
.hero-title{left:0;top:85px;width:720px;text-align:center;color:var(--white);font-size:16.5px;font-weight:500;line-height:22px}
.screen-frame{left:256px;top:144px;width:222px;height:133px;background:#2a2a2a;border-radius:6px;border:1px solid #777}
.screen{left:263px;top:151px;width:208px;height:110px;background:radial-gradient(circle at 50% 55%,#ffffff 0%,#e6e6e6 55%,#bdbdbd 100%)}
.screen-text{left:263px;top:174px;width:208px;text-align:center;font-size:9.5px;color:#333}
.screen-text b{color:#101a8a}
.screen-brand{left:263px;top:225px;width:208px;text-align:center;font-size:14px;color:var(--brand-gray)}
.player-bar{left:263px;top:255px;width:208px;height:10px;background:#1d1d1d}
.laptop-base{left:233px;top:276px;width:244px;height:6px;background:linear-gradient(#e8e8e8,#9a9a9a);border-radius:0 0 6px 6px}
.cta{left:301px;top:292px;width:97px;height:14px;background:var(--accent-red);border:1px solid #6b0a14;border-radius:8px;color:var(--ink);font-size:8.5px;font-weight:700;text-align:center;line-height:13px}

/* outcomes */
.outcomes{left:0;top:310px;width:720px;height:41px;background:var(--sky)}
.outcome{font-size:11px;font-weight:600;color:var(--navy);display:flex;align-items:center;gap:5px}
.outcome::before{content:"";width:10px;height:10px;border-radius:50%;background:var(--navy)}

/* features */
.section-title{left:0;top:374px;width:720px;text-align:center;font-size:16px;font-weight:700}
.feature-card{top:418px;width:127px;height:190px;border:1.5px solid #7c7a86;border-radius:10px;padding:30px 6px 0 7px;font-size:10.2px;line-height:12.2px;color:#1a1a1a}
.feature-card.purple{background:var(--brand-purple)}
.feature-card.lilac{background:var(--lilac)}
.feature-icon{top:401px;width:42px;height:42px;border-radius:50%;background:var(--white);border:1.5px solid #8b86a0}

/* proof */
.proof{left:0;top:626px;width:720px;height:425px;background:var(--lilac)}
.chart-panel{background:var(--white);border:2px solid #3a3a3a}
.testimonials-title{left:0;top:890px;width:720px;text-align:center;font-size:15.5px;font-weight:600}
.quote-mark{font-family:'Libre Baskerville',serif;font-size:72px;color:#dde3f2;line-height:1}
.quote-text{left:184px;top:914px;width:340px;text-align:center;font-family:'Libre Baskerville',serif;font-style:italic;font-size:7px;line-height:14.5px;color:#2b2b2b}
.dots{left:342px;top:951px;display:flex;gap:5px}
.dots span{width:4px;height:4px;border-radius:50%;background:#111}
.dots span.on{background:#8bc34a}
.portrait{top:960px;width:90px;height:90px;border-radius:50%;border:1.5px solid #444}
.portrait-name{left:313px;top:1025px;width:90px;text-align:center;font-family:'Libre Baskerville',serif;font-style:italic;font-size:11px;color:#111}

/* footer */
.site-footer{left:0;top:1051px;width:720px;height:149px;background:var(--footer);color:var(--white)}
.social-foot{left:299px;top:1102px;display:flex;gap:6px}
.social-foot span{width:19px;height:19px;border-radius:50%}
.footer-nav{left:0;top:1141px;width:720px;text-align:center;font-size:12.5px}
.copyright{left:0;top:1177px;width:720px;text-align:center;font-size:8.5px}
</style>
</head>
<body>

<header class="site-header abs">
  <div class="brand abs">kelbro</div>
  <div class="search abs">Enter your search keyword...</div>
  <div class="search-btn abs">
    <svg width="32" height="17" viewBox="0 0 32 17"><circle cx="15" cy="7.5" r="4.5" fill="none" stroke="#222" stroke-width="1.2"/><line x1="18.3" y1="10.8" x2="21.5" y2="14" stroke="#222" stroke-width="1.3"/></svg>
  </div>
  <div class="social-top abs"><span></span><span></span><span></span><span></span></div>
  <svg class="login-icon abs" width="14" height="16" viewBox="0 0 14 16"><circle cx="7" cy="5" r="3.5" fill="none" stroke="#222" stroke-width="1.2"/><path d="M1 15c0-4 2.5-5.5 6-5.5s6 1.5 6 5.5z" fill="none" stroke="#222" stroke-width="1.2"/></svg>
  <div class="login abs" style="left:610px">Log in<br>Regster</div>
  <div class="email abs">
    <svg width="16" height="12" viewBox="0 0 16 12"><rect x=".6" y=".6" width="14.8" height="10.8" fill="none" stroke="#222" stroke-width="1.1"/><path d="M.6 .6 8 7l7.4-6.4" fill="none" stroke="#222" stroke-width="1.1"/></svg>
    info@kelbro.com
  </div>
  <nav class="header-links abs"><span>Request a Demo</span><span>Links</span></nav>
</header>

<section class="hero abs" aria-label="Introduction"></section>
<h1 class="hero-title abs">A simple software tool that makes<br>your business goals actionable.</h1>
<div class="screen-frame abs"></div>
<div class="screen abs"></div>
<p class="screen-text abs">Give <b>Waypoint</b> a try for free today</p>
<svg class="abs" style="left:345px;top:186px" width="44" height="44" viewBox="0 0 44 44"><circle cx="22" cy="22" r="20" fill="none" stroke="#fff" stroke-width="2.5"/><path d="M17 14v16l13-8z" fill="#fff"/></svg>
<div class="screen-brand abs">kelbro</div>
<div class="player-bar abs">
  <svg width="208" height="10" viewBox="0 0 208 10"><line x1="18" y1="5" x2="170" y2="5" stroke="#555" stroke-width="1"/><line x1="18" y1="5" x2="40" y2="5" stroke="#9ccc3a" stroke-width="1.5"/><circle cx="40" cy="5" r="1.6" fill="#9ccc3a"/><rect x="188" y="3" width="9" height="4" fill="#9ccc3a"/><rect x="178" y="3" width="4" height="4" fill="#9ccc3a"/></svg>
</div>
<div class="laptop-base abs"></div>
<div class="cta abs">START NOW</div>

<section class="outcomes abs" aria-label="Outcomes">
  <div class="outcome abs" style="left:87px;top:8px">Define the outcomes</div>
  <div class="outcome abs" style="left:228px;top:8px">Set the Direction</div>
  <div class="outcome abs" style="left:363px;top:8px">Focus the Resources</div>
  <div class="outcome abs" style="left:510px;top:8px">Reduce the Risk</div>
  <div class="outcome abs" style="left:285px;top:28px">Increase Team Engagement</div>
</section>

<h2 class="section-title abs">What Makes Waypoint Different?</h2>
<div class="feature-card purple abs" style="left:70px">We want you to spend time thinking about and planning for your organization's success, not learning yet another tool. Waypoint has a modern UI making it more intuitive.</div>
<div class="feature-card lilac abs" style="left:219px">We want you to spend time thinking about and planning for your organization's success, not learning yet another tool. Waypoint has a modern UI making it more intuitive.</div>
<div class="feature-card purple abs" style="left:369px">We want you to spend time thinking about and planning for your organization's success, not learning yet another tool. Waypoint has a modern UI making it more intuitive.</div>
<div class="feature-card lilac abs" style="left:519px">We want you to spend time thinking about and planning for your organization's success, not learning yet another tool. Waypoint has a modern UI making it more intuitive.</div>

<div class="feature-icon abs" style="left:113px"><svg width="39" height="39" viewBox="0 0 39 39"><rect x="13" y="7" width="13" height="24" rx="2" fill="none" stroke="var(--brand-purple)" stroke-width="2"/><circle cx="19.5" cy="27.5" r="1.2" fill="var(--brand-purple)"/></svg></div>
<div class="feature-icon abs" style="left:261px"><svg width="39" height="39" viewBox="0 0 39 39" fill="none" stroke="var(--brand-purple)" stroke-width="1.8"><line x1="19.5" y1="8" x2="19.5" y2="30"/><line x1="9" y1="14" x2="30" y2="11"/><path d="M6 22l4-8 4 8a4 4 0 0 1-8 0z"/><path d="M25 19l4-8 4 8a4 4 0 0 1-8 0z"/><line x1="14" y1="30" x2="25" y2="30"/></svg></div>
<div class="feature-icon abs" style="left:412px"><svg width="39" height="39" viewBox="0 0 39 39" fill="none" stroke="var(--brand-purple)" stroke-width="2.2"><circle cx="19.5" cy="19.5" r="13"/><circle cx="19.5" cy="19.5" r="8"/><circle cx="19.5" cy="19.5" r="3" fill="var(--brand-purple)"/></svg></div>
<div class="feature-icon abs" style="left:563px"><svg width="39" height="39" viewBox="0 0 39 39" fill="none" stroke="var(--brand-purple)" stroke-width="2"><rect x="6" y="12" width="16" height="8" rx="4" transform="rotate(45 14 16)"/><rect x="17" y="19" width="16" height="8" rx="4" transform="rotate(45 25 23)"/></svg></div>

<section class="proof abs" aria-label="Results and testimonials"></section>

<div class="chart-panel abs" style="left:209px;top:647px;width:313px;height:115px">
  <svg width="309" height="111" viewBox="0 0 309 111" font-family="Montserrat, sans-serif">
    <text x="5" y="7" font-size="4.5" fill="#333">Project Cost Breakdown</text>
    <line x1="0" y1="10" x2="309" y2="10" stroke="#ddd" stroke-width=".6"/>
    <g font-size="3" fill="#444" text-anchor="end">
      <text x="30" y="27">$1,200,000</text><text x="30" y="41">$1,000,000</text><text x="30" y="55">$800,000</text>
      <text x="30" y="69">$600,000</text><text x="30" y="83">$400,000</text><text x="30" y="97">$200,000</text>
    </g>
    <line x1="32" y1="24" x2="32" y2="109" stroke="#444" stroke-width=".5"/>
    <line x1="32" y1="109" x2="300" y2="109" stroke="#444" stroke-width=".5"/>
    <g fill="#0a12e6">
      <rect x="39" y="57" width="23" height="52"/><rect x="77" y="57" width="23" height="52"/>
      <rect x="116" y="75" width="23" height="34"/><rect x="155" y="103" width="23" height="6"/>
      <rect x="193" y="104" width="23" height="5"/><rect x="232" y="106" width="23" height="3"/>
      <rect x="270" y="107.5" width="23" height="1.5"/>
    </g>
    <g fill="#f20d0d">
      <rect x="39" y="28" width="23" height="29"/><rect x="77" y="50" width="23" height="7"/>
      <rect x="116" y="70" width="23" height="5"/><rect x="155" y="99" width="23" height="4"/>
      <rect x="193" y="98" width="23" height="6"/><rect x="232" y="102" width="23" height="4"/>
      <rect x="270" y="105" width="23" height="2.5"/>
    </g>
    <rect x="268" y="22" width="36" height="13" fill="#fff" stroke="#ccc" stroke-width=".4"/>
    <rect x="271" y="25" width="3" height="3" fill="#0a12e6"/><text x="276" y="28" font-size="3">External Cost</text>
    <rect x="271" y="30" width="3" height="3" fill="#f20d0d"/><text x="276" y="33" font-size="3">Internal Cost</text>
  </svg>
</div>

<div class="chart-panel abs" style="left:210px;top:770px;width:312px;height:114px">
  <svg width="308" height="110" viewBox="0 0 308 110" font-family="Montserrat, sans-serif">
    <text x="10" y="8" font-size="4" fill="#333">Strategic Value Summary</text>
    <line x1="5" y1="12" x2="290" y2="12" stroke="#ddd" stroke-width=".6"/>
    <line x1="22" y1="20" x2="22" y2="104" stroke="#333" stroke-width=".5"/>
    <line x1="22" y1="104" x2="280" y2="104" stroke="#333" stroke-width=".5"/>
    <line x1="22" y1="67" x2="280" y2="67" stroke="#999" stroke-width=".5"/>
    <g font-size="2.8" fill="#444" text-anchor="end">
      <text x="19" y="26">3.5</text><text x="19" y="40">2.5</text><text x="19" y="54">1.5</text><text x="19" y="68">0</text><text x="19" y="82">-1</text><text x="19" y="96">-2</text>
    </g>
    <text x="26" y="65" font-size="2.8" fill="#555">No Strategic Value</text>
    <text x="268" y="102" font-size="2.8" fill="#555" text-anchor="end">Duration in months</text>
    <circle cx="48" cy="50" r=".8" fill="#999"/><circle cx="67" cy="66" r=".9" fill="#8aa"/>
    <circle cx="100" cy="60" r="1.2" fill="#999"/><circle cx="118" cy="52" r="1.3" fill="#999"/>
    <circle cx="204" cy="53" r="11" fill="#f0a6d6" opacity=".9"/>
    <circle cx="190" cy="53" r="8.5" fill="#e6737a" opacity=".85"/>
    <circle cx="289" cy="52" r="5.5" fill="#7fb3df" transform="translate(-18 0)"/>
  </svg>
</div>

<h2 class="testimonials-title abs">Testimonials</h2>
<div class="quote-mark abs" style="left:142px;top:896px">&ldquo;</div>
<div class="quote-mark abs" style="left:527px;top:913px">&rdquo;</div>
<p class="quote-text abs">This is the studio's version of Lorem Ipsum. Proin gravida nibh vel velit auctor aliquet. Aenean sollicitudin, lorem quis bibendum auctor, nisi elit consequat ipsum, nec sagittis sem nibh id elit. Duis sed odio sit amet nibh vulputate cursus a sit amet mauris. Morbi accumsan ipsum velit. Nam nec tellus</p>
<div class="dots abs"><span></span><span class="on"></span><span></span></div>
<div class="portrait abs" style="left:210px;background:radial-gradient(circle at 50% 45%,#cfcfcf,#4a4a4a)" role="img" aria-label="Portrait photo of a customer"></div>
<div class="portrait abs" style="left:313px;background:linear-gradient(#b8895f 0%,#c99a70 55%,#5f9a3a 78%,#5f9a3a 100%)" role="img" aria-label="Portrait photo of Daniel M."></div>
<div class="portrait-name abs">Daniel M.</div>
<div class="portrait abs" style="left:416px;background:radial-gradient(circle at 50% 45%,#e0e0e0,#555)" role="img" aria-label="Portrait photo of a customer"></div>

<footer class="site-footer abs">
  <div class="social-foot abs" style="top:51px">
    <span style="background:#3b5a9a"></span><span style="background:#1d9bd8"></span><span style="background:#0e76a8"></span>
    <span style="background:#c8232c"></span><span style="background:#3f6e9a"></span><span style="background:#e8781c"></span>
  </div>
  <nav class="footer-nav abs" style="top:90px">Resources Chronicles Support FAQ Terms of Service Pricing About</nav>
  <p class="copyright abs" style="top:126px">Copyright (c) 2017 www.kelbro.com All Rights Reserved</p>
</footer>

</body>
</html>
```